Business Card Design

We sell fish products to corporate food companies who then turn these products into final food products for consumers

Industry/Entity Type

Business

Contact Information for Business Card

I need a corporate business card template for a fish products business. We would like it be professional for use in dealing with multi national companies. This company business card template will be used by multiple employees so the following fields must be open to edit (Name, Phone Number and Email address)

```html
<!DOCTYPE html>
<html lang="en">
<head>
<meta charset="utf-8">
<title>Clear Harbor Seafoods – Business Card</title>
<link rel="stylesheet" href="https://fonts.googleapis.com/css2?family=Marcellus&family=Questrial&display=swap">
<style>
  :root {
    --page-bg: #ffffff;
    --card-bg: #2a2c2d;
    --brand-blue: #2f6fe8;
    --field-green: #cdf3c6;
    --detail-grey: #e4e6e6;
    --sun-blue: #2a73e0;
  }
  html, body {
    margin: 0;
    padding: 0;
    width: 1200px;
    height: 611px;
    overflow: hidden;
    background: var(--page-bg);
  }
  .canvas {
    position: relative;
    width: 1200px;
    height: 611px;
  }
  .card {
    position: absolute;
    background: var(--card-bg);
    overflow: hidden;
  }
  .card--front {
    left: 86px;
    top: 170px;
    width: 485px;
    height: 283px;
  }
  .card--back {
    left: 597px;
    top: 172px;
    width: 477px;
    height: 278px;
  }
  .company-name {
    position: absolute;
    left: 0;
    right: 0;
    top: 22px;
    margin: 0;
    text-align: center;
    font-family: "Marcellus", serif;
    font-weight: 400;
    font-size: 40px;
    line-height: 44px;
    letter-spacing: 1px;
    color: var(--brand-blue);
  }
  .employee-fields {
    position: absolute;
    left: 84px;
    top: 138px;
    margin: 0;
    padding: 0;
    list-style: none;
    font-family: "Questrial", sans-serif;
    font-size: 22px;
    line-height: 29px;
    color: var(--field-green);
  }
  .employee-fields .field--title { padding-left: 2px; }
  .employee-fields .field--email { padding-left: 6px; }
  .employee-fields .field--phone { padding-left: 3px; }
  .company-address {
    position: absolute;
    right: 30px;
    top: 165px;
    margin: 0;
    text-align: right;
    font-style: normal;
    font-family: "Questrial", sans-serif;
    font-size: 13px;
    line-height: 18px;
    color: var(--detail-grey);
  }
  .back-mark {
    position: absolute;
    left: 0;
    right: 0;
    top: 0;
    bottom: 0;
    display: flex;
    flex-direction: column;
    align-items: center;
    justify-content: center;
    gap: 18px;
  }
  .back-mark__circle {
    width: 96px;
    height: 96px;
    border-radius: 50%;
    background: var(--sun-blue);
  }
  .back-mark__name {
    margin: 0;
    font-family: "Marcellus", serif;
    font-weight: 400;
    font-size: 30px;
    letter-spacing: 1px;
    color: var(--brand-blue);
  }
</style>
</head>
<body>
  <main class="canvas">
    <section class="card card--front" aria-label="Business card front">
      <h1 class="company-name">CLEAR HARBOR<br>SEAFOODS</h1>
      <ul class="employee-fields">
        <li class="field--name">Name</li>
        <li class="field--title">TITLE</li>
        <li class="field--email">EMAIL</li>
        <li class="field--phone">Phone</li>
      </ul>
      <address class="company-address">
        Clear Harbor Seafoods<br>
        4818 Harbor Mill Road<br>
        Millbrook, KY 42000 USA<br>
        www.clearharborusa.com
      </address>
    </section>
    <section class="card card--back" aria-label="Business card back">
      <div class="back-mark">
        <div class="back-mark__circle"></div>
        <p class="back-mark__name">CLEAR HARBOR SEAFOODS</p>
      </div>
    </section>
  </main>
</body>
</html>
```